DOG DAYCARE BILLBOARD

Design a bold exciting billboard that can be read easily from a distance! Our goal is brand awareness and showcasing the services we offer (Boarding, Grooming, Daycare, and Training.
we would like to see examples with the phrase "your best friend's best day". Our name Bright Meadow Canine Activity Center (or just Bright Meadow might work better and could be bigger) and the services we provide.
(there are two examples of what we like included in the pictures)
you can find more information o our website at pawplayhouse@mailbox-example.com.

```html
<!DOCTYPE html>
<html lang="en">
<head>
<meta charset="utf-8">
<title>Bright Meadow Canine Activity Center — Billboard</title>
<link rel="stylesheet" href="https://fonts.googleapis.com/css2?family=Anton&family=Montserrat:wght@600;700;800&display=swap">
<style>
  :root {
    --yellow: #dcd400;
    --black: #000000;
    --white: #ffffff;
    --page: #e6e6e6;
    --dog-tan: #b5622a;
    --dog-cream: #e9e1d6;
  }
  * { margin: 0; padding: 0; box-sizing: border-box; }
  html, body { width: 1014px; height: 1200px; overflow: hidden; }
  body {
    background: var(--page);
    font-family: "Montserrat", Arial, sans-serif;
    position: relative;
  }
  .billboard {
    position: absolute;
    left: 37px;
    top: 450px;
    width: 940px;
    height: 368px;
    background: var(--yellow);
  }
  .dog-photo {
    position: absolute;
    left: 25px;
    top: -70px;
    width: 278px;
    height: 322px;
    border-radius: 90px 110px 0 0;
    background: linear-gradient(160deg, var(--dog-tan) 0%, var(--dog-tan) 38%, var(--dog-cream) 62%, var(--dog-cream) 100%);
  }
  .services-tab {
    position: absolute;
    left: 0;
    top: 251px;
    width: 940px;
    height: 117px;
  }
  .services-title {
    position: absolute;
    left: 24px;
    top: 272px;
    font-size: 26px;
    font-weight: 700;
    color: var(--yellow);
    white-space: nowrap;
  }
  .services-list {
    position: absolute;
    left: 24px;
    top: 320px;
    display: flex;
    align-items: center;
    gap: 12px;
    list-style: none;
    font-size: 21.5px;
    font-weight: 700;
    color: var(--white);
    white-space: nowrap;
  }
  .services-list li { display: flex; align-items: center; gap: 12px; }
  .paw { width: 18px; height: 18px; fill: var(--yellow); }
  .headline {
    position: absolute;
    left: 313px;
    top: 22px;
    font-family: "Anton", Impact, sans-serif;
    font-size: 98px;
    line-height: 91px;
    color: var(--black);
    text-transform: uppercase;
    letter-spacing: -0.5px;
  }
  .brand {
    position: absolute;
    left: 676px;
    top: 150px;
    width: 244px;
    display: flex;
    align-items: center;
    gap: 8px;
  }
  .brand-dot { width: 18px; height: 18px; border-radius: 50%; background: var(--black); flex: none; }
  .brand-name {
    font-size: 24px;
    font-weight: 800;
    color: var(--black);
    line-height: 1;
    white-space: nowrap;
  }
  .contact {
    position: absolute;
    left: 674px;
    top: 228px;
    color: var(--black);
  }
  .contact-row { display: flex; align-items: center; gap: 6px; white-space: nowrap; }
  .phone { font-size: 27px; font-weight: 800; }
  .web { font-size: 12.5px; font-weight: 700; margin-top: 2px; }
  .icon { width: 18px; height: 18px; flex: none; }
  .address {
    position: absolute;
    left: 634px;
    top: 310px;
    display: flex;
    align-items: center;
    gap: 10px;
    color: var(--white);
    font-size: 12.5px;
    font-weight: 600;
    line-height: 21px;
    white-space: nowrap;
  }
  .address .pin { width: 20px; height: 22px; flex: none; }
</style>
</head>
<body>
  <section class="billboard">
    <div class="dog-photo" role="img" aria-label="Photo of a tan and white dog raising one paw in a wave"></div>

    <svg class="services-tab" viewBox="0 0 940 117" aria-hidden="true">
      <path d="M0 0 H290 Q300 0 306 8 L330 40 Q336 49 348 49 H940 V117 H0 Z" fill="#000"/>
    </svg>

    <h1 class="headline">Your Best<br>Friend's<br>Best Day</h1>

    <div class="brand">
      <span class="brand-dot"></span>
      <span class="brand-name">Bright Meadow</span>
    </div>

    <div class="contact">
      <div class="contact-row phone">
        <svg class="icon" viewBox="0 0 20 20"><circle cx="10" cy="10" r="10" fill="#000"/><path d="M6.5 5.5l2 0 .8 2.3-1.2.9a6 6 0 0 0 3.2 3.2l.9-1.2 2.3.8v2a1 1 0 0 1-1 1A8.5 8.5 0 0 1 5.5 6.5a1 1 0 0 1 1-1z" fill="var(--yellow)"/></svg>
        <span>(555) 018-2746</span>
      </div>
      <div class="contact-row web">
        <svg class="icon" viewBox="0 0 20 20"><circle cx="10" cy="10" r="10" fill="#000"/><circle cx="10" cy="10" r="5.5" fill="none" stroke="var(--yellow)" stroke-width="1.2"/><ellipse cx="10" cy="10" rx="2.3" ry="5.5" fill="none" stroke="var(--yellow)" stroke-width="1.1"/><path d="M4.5 10h11" stroke="var(--yellow)" stroke-width="1.1"/></svg>
        <span>www.brightmeadowdogs.example</span>
      </div>
    </div>

    <p class="services-title">Services We Offer</p>
    <ul class="services-list">
      <li><svg class="paw" viewBox="0 0 20 20"><ellipse cx="10" cy="13.5" rx="4.5" ry="4"/><circle cx="4" cy="8.5" r="2"/><circle cx="16" cy="8.5" r="2"/><circle cx="7.3" cy="4.5" r="2"/><circle cx="12.7" cy="4.5" r="2"/></svg>Boarding</li>
      <li><svg class="paw" viewBox="0 0 20 20"><ellipse cx="10" cy="13.5" rx="4.5" ry="4"/><circle cx="4" cy="8.5" r="2"/><circle cx="16" cy="8.5" r="2"/><circle cx="7.3" cy="4.5" r="2"/><circle cx="12.7" cy="4.5" r="2"/></svg>Daycare</li>
      <li><svg class="paw" viewBox="0 0 20 20"><ellipse cx="10" cy="13.5" rx="4.5" ry="4"/><circle cx="4" cy="8.5" r="2"/><circle cx="16" cy="8.5" r="2"/><circle cx="7.3" cy="4.5" r="2"/><circle cx="12.7" cy="4.5" r="2"/></svg>Grooming</li>
      <li><svg class="paw" viewBox="0 0 20 20"><ellipse cx="10" cy="13.5" rx="4.5" ry="4"/><circle cx="4" cy="8.5" r="2"/><circle cx="16" cy="8.5" r="2"/><circle cx="7.3" cy="4.5" r="2"/><circle cx="12.7" cy="4.5" r="2"/></svg>Training</li>
    </ul>

    <div class="address">
      <svg class="pin" viewBox="0 0 20 22"><path d="M10 1a7.5 7.5 0 0 0-7.5 7.5C2.5 14 10 21 10 21s7.5-7 7.5-12.5A7.5 7.5 0 0 0 10 1z" fill="var(--yellow)"/><circle cx="10" cy="8.5" r="2.8" fill="#000"/></svg>
      <p>Bright Meadow Canine Activity Center<br>418 Orchard Ln. Maple Grove, ST 00000</p>
    </div>
  </section>
</body>
</html>
```